Automotive Repair Centre - Flyer Design

Bremwick Motors Cumbernauld are looking for a completely new flyer design for our blossoming auto repair centre. We are looking for bold eye catching designs as these flyers will be letterbox dropped around the local community. Approx. 10k per month. These will be printed double sided, on A5, with different print front and rear. Currently the whole rear is dedicated to servicing only, but this can be changed.

Our business prides itself on providing a high quality service so they flyer needs to convey this message. Also we believe in fair prices so they flyer also needs to convey this message in the design. Colour scheme is currently blue, yellow, and black. If possible it would be good to include the Drivemarq logo and the KELP logo.

We like the "specials" list from the Halvorn Drake flyer that is attached. We also like the clean look and layout of the other flyer that is uploaded. It would be good to include a special area for winter tyres much like is shown in the 50% off wheel alignment piece of the flyer attached.

Our current flyer uses the font GoodTimes as we would like this to remain if possible. It can be changed if the designer prefers. You can visit our website www.bremwick.co.uk for more information about our business.
Updates

Reason: Not had enough good designs to choose from yet.

Reason: Still not enough good designs to choose from

Reason: designs not up to the standard required.

Reason: Not enough designs that capture the brief have been submitted

Reason: looking for more designs

Reason: looking for some more bright designs. please read the brief!!!

Reason: same as before

Target Market(s)

General public.

Industry/Entity Type

Wheel

Requirements
Should not have
• We feel the flyer should not have photos of high end vehicles like Zantellis etc as the does not fit our approach of good value.

```html
<!DOCTYPE html>
<html lang="en">
<head>
<meta charset="utf-8">
<title>Bremwick Motors – Fixed Price Service</title>
<link rel="stylesheet" href="https://fonts.googleapis.com/css2?family=PT+Sans:wght@400;700&family=PT+Sans+Narrow:wght@700&display=swap">
<style>
  :root {
    --navy-deep: #0a0f3a;
    --navy: #141c62;
    --blue: #1f3a9c;
    --blue-bright: #2f5fc4;
    --yellow: #fff200;
    --tag-yellow: #f7cf14;
    --tag-card: #f4eedf;
    --price-red: #e2212b;
    --white: #ffffff;
  }
  * { box-sizing: border-box; margin: 0; padding: 0; }
  html, body {
    width: 846px; height: 1200px; overflow: hidden;
    background: var(--navy-deep);
  }
  .flyer {
    position: relative;
    width: 846px; height: 1200px; overflow: hidden;
    font-family: "PT Sans", sans-serif;
    color: var(--white);
    background:
      repeating-linear-gradient(180deg, rgba(255,255,255,0.05) 0 2px, transparent 2px 9px, rgba(0,0,0,0.12) 9px 12px, transparent 12px 19px),
      radial-gradient(ellipse 75% 40% at 50% 52%, var(--blue-bright) 0%, var(--blue) 35%, var(--navy) 70%, var(--navy-deep) 100%);
  }
  .brand {
    position: absolute; left: 70px; top: 120px;
    display: flex; align-items: center; gap: 14px;
  }
  .brand-mark {
    width: 30px; height: 30px; border-radius: 50%;
    background: var(--yellow);
  }
  .brand-name {
    font-size: 62px; font-weight: 700; letter-spacing: 1px;
    color: var(--white);
  }
  .headline {
    position: absolute; right: 34px; top: 26px;
    font-family: "PT Sans Narrow", sans-serif; font-weight: 700;
    color: var(--yellow); text-align: right; line-height: 0.86;
  }
  .headline-big { display: block; font-size: 124px; }
  .headline-mid { display: block; font-size: 92px; margin-top: 4px; }
  .headline-note { display: block; font-size: 23px; line-height: 1; margin-top: 8px; }
  .truck-art {
    position: absolute; left: 34px; top: 305px; width: 352px; height: 308px;
    border-radius: 40px 60px 30px 30px;
    background: linear-gradient(180deg, #e9b98a 0%, #dfa575 35%, #c4252c 55%, #a81d23 100%);
  }
  .price-tag { position: absolute; left: 400px; top: 350px; width: 430px; height: 280px; }
  .offer-list {
    position: absolute; top: 700px; left: 0; width: 846px;
    display: grid; grid-template-columns: 462px 384px;
    list-style: none;
  }
  .offer-list li {
    position: relative; font-size: 30px; line-height: 39px;
    padding-left: 69px; white-space: nowrap;
  }
  .offer-list li:nth-child(even) { padding-left: 27px; }
  .offer-list li::before {
    content: ""; position: absolute; top: 17px; left: 38px;
    width: 12px; height: 12px; border-radius: 50%; background: var(--yellow);
  }
  .offer-list li:nth-child(even)::before { left: 0; }
  .website-note {
    position: absolute; top: 900px; left: 0; width: 846px;
    text-align: center; font-size: 31px;
  }
  .contact {
    position: absolute; right: 21px; top: 1038px;
    text-align: right; font-size: 28px; line-height: 38px;
  }
  .address {
    position: absolute; left: 63px; top: 1158px;
    font-size: 23px; white-space: nowrap;
  }
  .base-rule {
    position: absolute; left: 0; bottom: 0; width: 846px; height: 6px;
    background: var(--yellow);
  }
</style>
</head>
<body>
<main class="flyer">
  <div class="brand">
    <span class="brand-mark"></span>
    <span class="brand-name">BREMWICK</span>
  </div>

  <h1 class="headline">
    <span class="headline-big">FIXED</span>
    <span class="headline-big">PRICE</span>
    <span class="headline-mid">SERVICE</span>
    <span class="headline-note">ANY VEHICLE UP TO 2000CC</span>
  </h1>

  <div class="truck-art" role="img" aria-label="Cartoon illustration of a red vintage delivery truck with a tan canvas cover"></div>

  <svg class="price-tag" viewBox="0 0 430 280" aria-label="Price tag: £89">
    <g transform="rotate(10 215 140)">
      <polygon points="20,140 95,60 415,60 415,220 95,220" fill="var(--tag-yellow)"/>
      <circle cx="72" cy="140" r="22" fill="var(--navy)"/>
      <rect x="115" y="75" width="285" height="130" fill="var(--tag-card)"/>
      <text x="258" y="185" text-anchor="middle" font-family="PT Sans, sans-serif" font-size="128" fill="var(--price-red)">£89</text>
    </g>
    <path d="M70 150 C 40 190, 20 230, 0 260" stroke="#1f6b3a" stroke-width="2" fill="none"/>
  </svg>

  <ul class="offer-list">
    <li>SPARK PLUGS</li>
    <li>LONG LIFE OIL</li>
    <li>OIL FILTER</li>
    <li>AIR FILTER</li>
    <li>VEHICLE SAFETY CHECK</li>
    <li>CAR BATTERIES</li>
    <li>WELDING</li>
    <li>ALTERNATORS</li>
    <li>STARTER MOTORS</li>
    <li>FAULT DIAGNOSTICS</li>
  </ul>

  <p class="website-note">See our website for full detail.</p>

  <address class="contact" style="font-style:normal">
    Tel:&nbsp; 01236 840517<br>
    Email: sales@bremwick.co.uk<br>
    http://www.bremwick.co.uk
  </address>

  <p class="address">14-16 Carrick Way Braemore Industrial Estate Cumbernauld G68 4QT</p>

  <div class="base-rule"></div>
</main>
</body>
</html>
```